Business Cards Needed

Hi designers, I have a new logo that was created by one of the PixelHarbor designers. I'd now like to use that logo to make business cards. The company is called CarewiseMetrics Advisory and is a business consulting firm. I'd like the business cards to be horizontal, modern, and professional.
I'd like the following information to be on the business card:
1) Logo
2) my name - Janine Oulton
3) my title - Principal
4) name of business - CarewiseMetrics Advisory
5) mobile - 508.742.3391
6) e-mail - janine@carewisemetricsadvisory.example
I'm uploading a JPG file of the logo. I'm hoping this is the correct file format. Please let me know if you need another type of file. Thank you.

```html
<!DOCTYPE html>
<html lang="en">
<head>
<meta charset="utf-8">
<title>CarewiseMetrics Advisory – Business Card</title>
<link href="https://fonts.googleapis.com/css2?family=Roboto:wght@400;500;700&display=swap" rel="stylesheet">
<style>
  :root {
    --backdrop: #1e1e1e;
    --card-white: #f3f3f3;
    --brand-blue: #1475b9;
    --brand-green: #8cc43f;
    --ink: #333333;
    --white: #ffffff;
  }
  * { margin: 0; padding: 0; box-sizing: border-box; }
  html, body { width: 1200px; height: 1059px; overflow: hidden; }
  body {
    background: var(--backdrop);
    font-family: "Roboto", Arial, sans-serif;
    position: relative;
  }
  .card {
    position: absolute;
    width: 690px;
    height: 392px;
    border-radius: 24px;
    overflow: hidden;
  }
  .card-front { left: 256px; top: 89px; background: var(--card-white); }
  .card-back  { left: 254px; top: 547px; background: var(--brand-blue); }

  .front-wordmark {
    position: absolute;
    left: 58px; top: 178px;
    width: 270px;
    color: var(--brand-blue);
    font-weight: 500;
    font-size: 25px;
    line-height: 1.15;
  }
  .divider {
    position: absolute;
    left: 343px; top: 108px;
    width: 1.5px; height: 175px;
    background: var(--brand-blue);
  }
  .details { position: absolute; left: 369px; top: 104px; color: var(--ink); }
  .person-name {
    font-weight: 700;
    font-size: 27px;
    line-height: 1;
    letter-spacing: 0.2px;
  }
  .person-name .first { color: var(--brand-blue); }
  .person-name .last { color: var(--brand-green); }
  .person-title { font-size: 17px; margin-top: 6px; }
  .address { font-size: 16.5px; line-height: 23px; margin-top: 17px; }
  .contact-list { list-style: none; margin-top: 13px; }
  .contact-list li {
    display: flex; align-items: center; gap: 8px;
    font-size: 16.5px; height: 27px;
  }
  .contact-list li.email { font-size: 14.5px; }
  .contact-list svg { width: 12px; height: 12px; flex: none; }

  .footer-swoosh { position: absolute; left: 0; top: 0; }
  .website {
    position: absolute;
    right: 24px; top: 357px;
    color: var(--white);
    font-size: 16px;
  }

  .back-wordmark {
    position: absolute;
    left: 0; right: 0; top: 168px;
    text-align: center;
    color: var(--white);
    font-weight: 500;
    font-size: 46px;
    line-height: 1.2;
  }
</style>
</head>
<body>
  <section class="card card-front" aria-label="Business card front">
    <div class="front-wordmark">CarewiseMetrics<br>Advisory</div>
    <div class="divider"></div>
    <div class="details">
      <h1 class="person-name"><span class="first">JANINE</span> <span class="last">OULTON</span></h1>
      <p class="person-title">Principal</p>
      <p class="address">P.O. Box Linden Street<br>Country Name AB, K7R 2M4</p>
      <ul class="contact-list">
        <li>
          <svg viewBox="0 0 12 12" aria-hidden="true"><path fill="#8cc43f" d="M1 4.2C1 2.6 3.2 2 6 2s5 .6 5 2.2v.9H8.6V4H3.4v1.1H1zM3 6.5 4.2 5h3.6L9 6.5V10H3z"/></svg>
          <span>508.742.3391</span>
        </li>
        <li class="email">
          <svg viewBox="0 0 12 12" aria-hidden="true"><path fill="#8cc43f" d="M1 5 6 1.5 11 5v6H1zM2.2 5.6 6 8.2l3.8-2.6L6 3z"/></svg>
          <span>janine@carewisemetricsadvisory.example</span>
        </li>
      </ul>
    </div>
    <svg class="footer-swoosh" width="690" height="392" viewBox="0 0 690 392" aria-hidden="true">
      <path fill="var(--brand-green)" d="M80 392 Q360 340 630 335 L690 336 L690 339 Q380 342 126 392 Z"/>
      <path fill="var(--brand-blue)" d="M148 392 Q420 346 690 341 L690 392 Z"/>
    </svg>
    <p class="website">www.carewisemetricsadvisory.example</p>
  </section>

  <section class="card card-back" aria-label="Business card back">
    <div class="back-wordmark">CarewiseMetrics<br>Advisory</div>
  </section>
</body>
</html>
```